Author needs design for self-help relationship book

I need a book cover design for a self-help handbook on relationships called 'Seven quiet habits for building forever bonds with your partner - fast". The design should appeal in the main to young couples anywhere in the world.

```html
<!DOCTYPE html>
<html lang="en">
<head>
<meta charset="utf-8">
<title>Seven Quiet Habits for Building Forever Bonds – Book Cover</title>
<link href="https://fonts.googleapis.com/css2?family=Limelight&family=Poiret+One&display=swap" rel="stylesheet">
<style>
  :root {
    --paper: #ffffff;
    --ink: #0d0d0d;
    --brush: #0bc8f0;
    --brush-light: #6fdcf6;
    --haze: #fbf4ef;
    --skin-light: #f0d6c4;
    --skin-mid: #dcae92;
    --skin-deep: #c98f70;
    --shirt: #a9d3e3;
    --shirt-light: #d4eaf2;
  }
  html, body {
    margin: 0;
    padding: 0;
    width: 832px;
    height: 1200px;
    overflow: hidden;
    background: var(--paper);
  }
  .cover {
    position: relative;
    width: 832px;
    height: 1200px;
    overflow: hidden;
    background: var(--paper);
  }
  .cover-photo {
    position: absolute;
    inset: 0;
    background:
      radial-gradient(ellipse 300px 260px at 70px 110px, rgba(255,255,255,1) 0%, rgba(255,255,255,0.85) 40%, rgba(255,255,255,0) 100%),
      radial-gradient(ellipse 260px 360px at 800px 150px, rgba(255,255,255,0.95) 0%, rgba(255,255,255,0) 100%),
      linear-gradient(200deg, rgba(169,211,227,0) 45%, rgba(169,211,227,0.85) 75%, var(--shirt-light) 100%),
      linear-gradient(165deg, var(--haze) 0%, var(--skin-light) 22%, var(--skin-mid) 45%, var(--skin-deep) 62%, var(--skin-mid) 78%, var(--skin-light) 100%);
  }
  .brush-stroke {
    position: absolute;
    left: 0;
    top: 0;
    width: 832px;
    height: 1200px;
  }
  .author-name {
    position: absolute;
    top: 62px;
    left: 0;
    width: 100%;
    margin: 0;
    text-align: center;
    font-family: "Poiret One", sans-serif;
    font-size: 66px;
    font-weight: 400;
    letter-spacing: 12px;
    color: var(--ink);
    -webkit-text-stroke: 1.2px var(--ink);
    text-shadow: 0 0 3px #fff, 0 0 3px #fff, 2px 2px 0 #fff, -2px -2px 0 #fff, 2px -2px 0 #fff, -2px 2px 0 #fff;
  }
  .title {
    position: absolute;
    left: 40px;
    top: 600px;
    width: 640px;
    margin: 0;
    font-family: "Limelight", fantasy;
    font-weight: 400;
    font-size: 62px;
    line-height: 1.02;
    color: var(--ink);
    text-align: center;
    letter-spacing: 3px;
    transform: rotate(-16deg);
    transform-origin: center;
  }
  .title span { display: block; }
  .subtitle {
    position: absolute;
    left: 0;
    width: 100%;
    top: 1042px;
    margin: 0;
    text-align: center;
    font-family: "Poiret One", sans-serif;
    font-size: 66px;
    font-weight: 400;
    color: var(--ink);
    -webkit-text-stroke: 1px var(--ink);
  }
</style>
</head>
<body>
  <main class="cover">
    <div class="cover-photo" role="img" aria-label="Bright sunlit photograph of a smiling young couple leaning their heads together; she wears a white top, he wears a light blue t-shirt"></div>

    <svg class="brush-stroke" viewBox="0 0 832 1200" aria-hidden="true">
      <defs>
        <filter id="rough-edge" x="-5%" y="-5%" width="110%" height="110%">
          <feTurbulence type="fractalNoise" baseFrequency="0.035 0.09" numOctaves="3" seed="4"/>
          <feDisplacementMap in="SourceGraphic" scale="26"/>
        </filter>
      </defs>
      <g filter="url(#rough-edge)">
        <path fill="var(--brush)" d="M-20 780 L160 700 L330 560 L520 470 L690 440 L700 500 L610 560 L700 600 L650 660 L690 720 L560 790 L600 840 L430 920 L470 960 L270 1030 L100 1050 L-20 1040 Z"/>
        <path fill="var(--brush)" d="M-20 1020 L200 980 L140 1040 L30 1060 L-20 1060 Z"/>
      </g>
      <path fill="var(--brush-light)" opacity="0.45" d="M60 820 L260 700 L500 580 L630 545 L520 620 L300 740 L110 850 Z"/>
    </svg>

    <p class="author-name">AUTHOR NAME</p>

    <h1 class="title">
      <span>Seven Quiet Habits</span>
      <span>for Building</span>
      <span>Forever Bonds</span>
    </h1>

    <p class="subtitle">with your partner – fast</p>
  </main>
</body>
</html>
```